Business card design for strategy and management consulting company. Would like to have a clean and professional business card, based on the attached logo. The company is a strategy and management consulting company focusing on sustainable business modlels based on economic, social and environmental market opportunities. Preferably the logo should be included on both sides of the design.

Industry/Entity Type

Business

Contact Information for Business Card

Håvard Lilleby, CEO/Management consultant
havard.lilleby@quarvenpartners.example
Mob: +47 948 26 317
Office: Vikfjell gate 14, pb 312 sentrum, N-0172 Oslo Norway

Requirements
Must have
• Include attached logo
Nice to have
• Would like to have the logo on both sides
Should not have
• Many colours.

```html
<!DOCTYPE html>
<html lang="en">
<head>
<meta charset="utf-8">
<title>Quarven business card</title>
<link href="https://fonts.googleapis.com/css2?family=Open+Sans:wght@400;700&display=swap" rel="stylesheet">
<style>
  :root {
    --backdrop: #34424a;
    --card: #0a0a0a;
    --ink: #ffffff;
    --accent: #f2d21b;
  }
  html, body {
    margin: 0;
    padding: 0;
    width: 1200px;
    height: 900px;
    overflow: hidden;
    background: var(--backdrop);
    font-family: "Open Sans", sans-serif;
  }
  .canvas {
    width: 1200px;
    height: 900px;
    display: flex;
    flex-direction: column;
    align-items: center;
    justify-content: center;
    gap: 40px;
  }
  .card {
    width: 600px;
    height: 370px;
    background: var(--card);
    color: var(--ink);
    position: relative;
    box-sizing: border-box;
    overflow: hidden;
  }
  .card--front {
    display: flex;
    align-items: center;
    justify-content: center;
  }
  .wordmark {
    display: flex;
    align-items: flex-start;
    gap: 6px;
    font-weight: 700;
    color: var(--ink);
    line-height: 1;
  }
  .wordmark__name { letter-spacing: -1px; }
  .wordmark__dot {
    border-radius: 50%;
    background: var(--accent);
    flex: none;
  }
  .card--front .wordmark__name { font-size: 64px; }
  .card--front .wordmark__dot { width: 12px; height: 12px; margin-top: 6px; }
  .card--back {
    display: flex;
    align-items: center;
    padding-right: 24px;
  }
  .card--back .brand-side {
    width: 250px;
    flex: none;
    display: flex;
    justify-content: center;
  }
  .card--back .wordmark__name { font-size: 46px; }
  .card--back .wordmark__dot { width: 9px; height: 9px; margin-top: 4px; }
  .divider {
    width: 1px;
    height: 220px;
    flex: none;
    background: linear-gradient(to bottom, transparent, var(--ink) 20%, var(--ink) 80%, transparent);
  }
  .contact {
    padding-left: 24px;
    font-size: 13px;
    line-height: 1.4;
    min-width: 0;
  }
  .contact p { white-space: nowrap; }
  .contact__name {
    font-size: 24px;
    font-weight: 700;
    margin: 0;
    line-height: 1.1;
  }
  .contact__role {
    font-size: 13px;
    margin: 0 0 20px;
  }
  .contact__address { margin: 0 0 8px; }
  .contact__line {
    display: flex;
    align-items: center;
    gap: 9px;
    margin: 2px 0;
  }
  .contact__line svg { width: 13px; height: 13px; flex: none; }
</style>
</head>
<body>
<main class="canvas">
  <section class="card card--front" aria-label="Card front">
    <div class="wordmark">
      <span class="wordmark__name">Quarven</span>
      <span class="wordmark__dot"></span>
    </div>
  </section>

  <section class="card card--back" aria-label="Card back">
    <div class="brand-side">
      <div class="wordmark">
        <span class="wordmark__name">Quarven</span>
        <span class="wordmark__dot"></span>
      </div>
    </div>
    <div class="divider"></div>
    <div class="contact">
      <p class="contact__name">Håvard Lilleby</p>
      <p class="contact__role">CEO/Management consultant</p>
      <p class="contact__address">Vikfjell gate 14,<br>pb 312 sentrum, Oslo Norway</p>
      <p class="contact__line">
        <svg viewBox="0 0 14 14" aria-hidden="true"><rect x="3.5" y="0.5" width="7" height="13" rx="1.2" fill="none" stroke="#fff" stroke-width="1.3"/><rect x="5.5" y="10.5" width="3" height="1.3" fill="#fff"/></svg>
        <span>+47 948 26 317</span>
      </p>
      <p class="contact__line">
        <svg viewBox="0 0 14 14" aria-hidden="true"><rect x="0.5" y="3" width="13" height="9" fill="#fff"/><path d="M0.5 3 L7 8 L13.5 3" fill="none" stroke="#0a0a0a" stroke-width="1.2"/></svg>
        <span>havard.lilleby@quarvenpartners.example</span>
      </p>
    </div>
  </section>
</main>
</body>
</html>
```